Stonebay Towing Business Card

Towing
Accident towing
Mechanical breakdown
Insurance, salvage and recovery
4wd off road towing
Light & Heavy towing
8347 2516
24 hour business 7 days

Logo can be whole size on front

Industry/Entity Type

Towing/ transport

Contact Information for Business Card

The above

```html
<!DOCTYPE html>
<html lang="en">
<head>
<meta charset="utf-8">
<title>Stonebay Towing – Business Card</title>
<link rel="stylesheet" href="https://fonts.googleapis.com/css2?family=Montserrat:wght@500;600;700;800&display=swap">
<style>
  :root {
    --bg: #e6e6e8;
    --card: #ffffff;
    --ink: #141414;
    --red: #c8202a;
    --shadow: rgba(0, 0, 0, 0.18);
  }
  * { margin: 0; padding: 0; box-sizing: border-box; }
  html, body {
    width: 1200px;
    height: 900px;
    overflow: hidden;
    background: var(--bg);
    font-family: "Montserrat", sans-serif;
    color: var(--ink);
  }
  .sheet {
    width: 1200px;
    height: 900px;
    display: flex;
    flex-direction: column;
    align-items: center;
    justify-content: center;
    gap: 44px;
  }
  .card {
    width: 640px;
    height: 366px;
    background: var(--card);
    box-shadow: 0 10px 28px var(--shadow);
    display: flex;
    flex-direction: column;
    align-items: center;
    justify-content: center;
    text-align: center;
  }
  .brand-name {
    font-weight: 800;
    color: var(--red);
    letter-spacing: 0.5px;
    line-height: 1;
  }
  .card--info .brand-name { font-size: 44px; margin-bottom: 26px; }
  .card--logo .brand-name { font-size: 64px; }

  .phone {
    display: flex;
    align-items: center;
    gap: 8px;
    font-size: 30px;
    font-weight: 700;
    line-height: 1;
  }
  .phone svg { width: 26px; height: 26px; }
  .hours {
    margin-top: 8px;
    font-size: 21px;
    font-weight: 700;
    color: var(--red);
  }
  .services {
    margin-top: 20px;
    font-size: 15px;
    font-weight: 600;
    line-height: 1.55;
  }
  .services .dot { color: var(--red); margin: 0 5px; }
</style>
</head>
<body>
<main class="sheet">
  <section class="card card--info">
    <div class="brand-name">Stonebay Towing</div>
    <div class="phone">
      <svg viewBox="0 0 24 24" aria-hidden="true">
        <path fill="#141414" d="M6.6 10.8c1.4 2.8 3.8 5.1 6.6 6.6l2.2-2.2c.3-.3.7-.4 1-.2 1.1.4 2.3.6 3.6.6.6 0 1 .4 1 1V20c0 .6-.4 1-1 1C10.6 21 3 13.4 3 4c0-.6.4-1 1-1h3.5c.6 0 1 .4 1 1 0 1.3.2 2.5.6 3.6.1.3 0 .7-.2 1l-2.3 2.2z"/>
        <path fill="none" stroke="#141414" stroke-width="1.6" stroke-linecap="round" d="M14 3.5a7 7 0 0 1 6.5 6.5M14 7a3.5 3.5 0 0 1 3 3"/>
      </svg>
      <span>8347 2516</span>
    </div>
    <div class="hours">24/7 Business</div>
    <div class="services">
      <div><span class="dot">•</span>Towing<span class="dot">•</span>Accident towing<span class="dot">•</span>Mechanical breakdown</div>
      <div><span class="dot">•</span>Insurance, salvage and recovery</div>
      <div><span class="dot">•</span>4wd off road towing<span class="dot">•</span>Light &amp; Heavy towing</div>
    </div>
  </section>

  <section class="card card--logo">
    <div class="brand-name">Stonebay Towing</div>
  </section>
</main>
</body>
</html>
```